Wed site for biomedical device startup

We need a generic website for a medical device startup. I will provide examples below of websites from other companies that can serve as models for what we are looking for. The startup is for a device that can non invasively measure blood flow in the brain using light. The application is to detect the type of stroke someone is having before they get to the hospital so treatment can be started right away. This saves patients upto hours of delayed treatment. Patients will be able to recover from stroke much better and faster as a result. I have attached an AI generated illustration of what the device will ultimately look like for reference.

https://www.brightvalemedical.com
https://quintavex.com

Target Market(s)

Biomedical, medical device, investors of biomedical device startups

Industry/Entity Type

Biomedical

Coding

Coded - Design and coding required

Number of Pages Required

4 page

Requirements
Must have
• same section and section headings as example websites listed above
Nice to have
• similar to example websites listed above. Prefer a darker website over a lighter one. Perhaps dark blues to go with logo colors. A moving background image element at top of landing page could be cool. Something indicative of heartbeat, or neurons, or blood flow.

```html
<!DOCTYPE html>
<html lang="en">
<head>
<meta charset="utf-8">
<title>NEUROVA – Smart Stroke Detection</title>
<link rel="stylesheet" href="https://fonts.googleapis.com/css2?family=Audiowide&family=Montserrat:wght@400;500;600;700&display=swap">
<style>
  :root{
    --bg-deep:#05052a;
    --bg-navy:#0a0a3d;
    --violet:#8a33d6;
    --sky:#3a9ee0;
    --lilac:#d9a6ff;
    --eyebrow:#3d8ee6;
    --white:#ffffff;
    --line:#3a3f8a;
    --card-border:#5a5fb0;
    --grad:linear-gradient(90deg,#8a2fd0 0%,#5a6ee0 60%,#3aa0e6 100%);
  }
  *{box-sizing:border-box;margin:0;padding:0}
  html,body{width:1200px;height:2751px;overflow:hidden}
  body{position:relative;background:var(--bg-deep);color:var(--white);font-family:"Montserrat",sans-serif}
  .abs{position:absolute}
  .display{font-family:"Audiowide",sans-serif;font-weight:400}

  /* header */
  .brand{display:flex;align-items:center;gap:8px;font-family:"Montserrat",sans-serif;font-weight:500;font-size:31px;letter-spacing:2px;color:var(--white)}
  .brand-dot{width:46px;height:46px;border-radius:50%;background:var(--grad)}
  .nav{left:599px;top:34px;display:flex;gap:22px;font-size:13px;font-weight:700}
  .nav a{color:var(--white);text-decoration:none}
  .nav a.active{color:#c878ff}
  .pill{display:flex;align-items:center;justify-content:center;border-radius:30px;background:var(--grad);border:2px solid #fff;font-weight:700;font-size:14px;color:#fff;text-decoration:none}

  /* hero */
  .hero{left:0;top:0;width:1200px;height:675px;background:
    radial-gradient(ellipse 700px 500px at 900px 300px,#1e4fd0 0%,transparent 70%),
    linear-gradient(180deg,#08083a 0%,#17207a 55%,#2a2a9a 100%)}
  .hero-art{left:700px;top:110px;width:470px;height:540px;border-radius:45% 45% 50% 50%/40% 40% 60% 60%;background:radial-gradient(circle at 50% 45%,rgba(255,140,80,.55),rgba(70,110,240,.35) 55%,transparent 80%)}
  .hero-title{left:111px;top:185px;font-size:50px;line-height:58px}
  .hero-title .accent{color:var(--lilac)}
  .hero-copy{left:111px;top:324px;width:450px;font-size:14px;font-weight:700;line-height:22.5px;text-transform:uppercase}

  /* technology */
  .tech-bg{left:0;top:675px;width:1200px;height:720px;background:
    radial-gradient(ellipse 400px 350px at 0 200px,rgba(120,50,200,.35),transparent 70%),
    radial-gradient(ellipse 350px 300px at 1200px 180px,rgba(60,110,220,.3),transparent 70%),var(--bg-deep)}
  .doctor{left:111px;top:862px;width:418px;height:418px;border-radius:50%;background:linear-gradient(90deg,#8a2fd0,#3a9ee0)}
  .eyebrow{font-size:26px;color:var(--eyebrow)}
  .h2{font-size:40px;line-height:47px}
  .feature-icon{width:78px;height:78px;border-radius:50%;border:2px solid #fff;background:var(--grad);display:flex;align-items:center;justify-content:center}
  .connector{left:636px;width:6px;border-left:2px solid #fff;border-right:2px solid #fff}
  .feature-title{font-size:16px;font-weight:600}
  .feature-desc{font-size:14.5px;line-height:23px;width:400px}

  /* partners */
  .center{left:0;width:1200px;text-align:center}
  .partner{top:1551px;width:215px;height:96px;border:1px solid var(--card-border);border-radius:4px;background:var(--bg-navy);display:flex;align-items:center;justify-content:center}
  .partner-badge{width:120px;height:36px;border-radius:6px;background:rgba(255,255,255,.85)}

  /* contact */
  .contact-bg{left:0;top:1660px;width:1200px;height:800px;background:
    radial-gradient(ellipse 300px 400px at 1200px 350px,rgba(120,50,200,.45),transparent 70%),
    radial-gradient(ellipse 500px 200px at 600px 150px,rgba(40,60,160,.3),transparent 70%)}
  .lead{font-size:15px;line-height:23px}
  .form-card{left:253px;top:1944px;width:694px;height:500px;border:1px solid var(--card-border);border-bottom:none;border-radius:6px 6px 0 0}
  .field{left:338px;width:524px;height:46px;border:2px solid #fff;border-radius:23px;background:#000;padding-left:24px;display:flex;align-items:center;font-size:11.5px;font-weight:500}
  .submit{left:338px;top:2294px;width:524px;height:46px;border-radius:23px;background:var(--grad);display:flex;align-items:center;justify-content:center;font-weight:700;font-size:14px}

  /* footer */
  .rule{left:137px;width:927px;height:1px;background:var(--line)}
  .foot-head{font-size:15px;font-weight:500}
  .foot-link{font-size:14px;line-height:26px}
  .copyright{font-size:14px}
</style>
</head>
<body>

<!-- Hero -->
<section class="abs hero"></section>
<div class="abs hero-art" role="img" aria-label="Glowing wireframe organ with a pulse line across it"></div>

<header>
  <div class="abs brand" style="left:115px;top:21px"><span class="brand-dot"></span>NEUROVA</div>
  <nav class="abs nav">
    <a class="active" href="#">HOME</a><a href="#">ABOUT</a><a href="#">TECHNOLOGY</a><a href="#">PRESS</a>
  </nav>
  <a class="abs pill" href="#" style="left:928px;top:18px;width:158px;height:47px">CONTACT US</a>
</header>

<h1 class="abs hero-title display">Smart Stroke<br><span class="accent">Type Detection</span></h1>
<p class="abs hero-copy">Non-invasive light-based technology that measures blood flow in the brain, identifying the stroke type before the hospital so treatment starts right away.</p>
<a class="abs pill" href="#" style="left:111px;top:447px;width:196px;height:47px">CONNECT WITH US</a>

<!-- Technology -->
<section class="abs tech-bg"></section>
<div class="abs doctor" role="img" aria-label="Doctor in a white coat holding a tablet, framed by a gradient circle"></div>

<p class="abs eyebrow display" style="left:603px;top:753px">Advanced Technology</p>
<h2 class="abs h2 display" style="left:603px;top:795px">Light-Based Brain Flow<br>Sensing</h2>

<div class="abs connector" style="top:1020px;height:48px"></div>
<div class="abs connector" style="top:1144px;height:48px"></div>

<div class="abs feature-icon" style="left:600px;top:941px">
  <svg width="38" height="34" viewBox="0 0 38 34" fill="none" stroke="#fff" stroke-width="1.6"><rect x="1" y="1" width="30" height="22" rx="2"/><polyline points="6,17 12,11 17,15 25,7"/><path d="M10 30h14M17 23v7"/><circle cx="31" cy="24" r="6"/><path d="M31 21v3l2 2"/></svg>
</div>
<p class="abs feature-title" style="left:700px;top:943px">PORTABLE SENSING</p>
<p class="abs feature-desc" style="left:700px;top:970px">Compact, non-invasive device that reads brain blood flow with light, anywhere, anytime.</p>

<div class="abs feature-icon" style="left:600px;top:1066px">
  <svg width="38" height="38" viewBox="0 0 38 38" fill="none" stroke="#fff" stroke-width="1.6"><rect x="3" y="2" width="30" height="32" rx="2"/><path d="M3 9h30M8 15h14M8 20h10"/><path d="M26 18l9 16H17z"/><path d="M26 24v5M26 31v1"/></svg>
</div>
<p class="abs feature-title" style="left:700px;top:1067px">REAL-TIME ALERTS</p>
<p class="abs feature-desc" style="left:700px;top:1094px">Stroke type results sent to the hospital team before the patient arrives.</p>

<div class="abs feature-icon" style="left:600px;top:1190px">
  <svg width="38" height="38" viewBox="0 0 38 38" fill="none" stroke="#fff" stroke-width="1.6"><circle cx="17" cy="9" r="6"/><path d="M6 26c0-6 5-10 11-10"/><path d="M3 30l8-4h10c2 0 2 3 0 3h-7M21 29l10-5c2-1 4 2 1 3l-12 7H8"/><circle cx="29" cy="18" r="5"/><path d="M29 15v6M26 18h6"/></svg>
</div>
<p class="abs feature-title" style="left:700px;top:1191px">PATIENT-CENTERED</p>
<p class="abs feature-desc" style="left:700px;top:1218px">Saves hours of delayed treatment for faster and better stroke recovery.</p>

<!-- Partners -->
<p class="abs center eyebrow display" style="top:1419px">Our Partners</p>
<h2 class="abs center h2 display" style="top:1462px">Partners and Collaborators</h2>
<div class="abs partner" style="left:15px"><span class="partner-badge"></span></div>
<div class="abs partner" style="left:254px"><span class="partner-badge"></span></div>
<div class="abs partner" style="left:492px"><span class="partner-badge"></span></div>
<div class="abs partner" style="left:731px"><span class="partner-badge"></span></div>
<div class="abs partner" style="left:969px"><span class="partner-badge"></span></div>

<!-- Contact -->
<section class="abs contact-bg"></section>
<p class="abs center eyebrow display" style="top:1745px">Contact us</p>
<h2 class="abs center h2 display" style="top:1787px">Stay Connected</h2>
<p class="abs center lead" style="top:1855px">Join our community to receive updates about our latest developments and research in<br>light-based stroke detection technology.</p>

<div class="abs form-card"></div>
<div class="abs field" style="top:2010px">FIRST NAME</div>
<div class="abs field" style="top:2081px">LAST NAME</div>
<div class="abs field" style="top:2151px">EMAIL</div>
<div class="abs field" style="top:2222px">COMPANY</div>
<div class="abs submit">SUBSCRIBE</div>

<!-- Footer -->
<div class="abs rule" style="top:2473px"></div>
<div class="abs brand" style="left:122px;top:2539px"><span class="brand-dot"></span>NEUROVA</div>

<p class="abs foot-head" style="left:443px;top:2536px">COMPANY</p>
<p class="abs foot-link" style="left:444px;top:2564px">About<br>Press</p>

<p class="abs foot-head" style="left:677px;top:2536px">LEGAL</p>
<p class="abs foot-link" style="left:679px;top:2564px">Privacy Policy<br>Terms of Service</p>

<p class="abs foot-head" style="left:911px;top:2534px">EMAIL</p>
<p class="abs foot-link" style="left:913px;top:2562px">info@companyname.com</p>

<div class="abs rule" style="top:2657px"></div>
<p class="abs center copyright" style="top:2677px">Copyright@2025.All Rights Reserved</p>

</body>
</html>
```